Business Card

I need a business card that really pops for a potential customer or person who refers a personal injury lead. I want to highlight our office locations, but only address that needs to be on the card is my office's main address. I want a sleek, modern and minimalist design.

```html
<!DOCTYPE html>
<html lang="en">
<head>
<meta charset="utf-8">
<title>Northgate Injury Counsel — Business Card</title>
<link href="https://fonts.googleapis.com/css2?family=Arimo:wght@400;700&display=swap" rel="stylesheet">
<style>
  :root {
    --backdrop: #e3e3e1;
    --card: #f2f2f1;
    --ink: #2d2d2d;
    --rule: #3a3a3a;
  }
  * { margin: 0; padding: 0; box-sizing: border-box; }
  html, body {
    width: 1200px; height: 1064px; overflow: hidden;
    background: var(--backdrop);
    font-family: "Arimo", Arial, sans-serif;
    color: var(--ink);
  }
  .card {
    position: absolute; left: 322px;
    width: 555px; height: 317px;
    background: var(--card);
    box-shadow: 0 1px 3px rgba(0,0,0,0.12);
  }
  .card--front { top: 194px; }
  .card--back { top: 553px; }

  .wordmark { position: absolute; font-weight: 400; color: var(--ink); line-height: 1; white-space: nowrap; }
  .card--front .wordmark { right: 36px; top: 48px; text-align: right; }
  .card--front .wordmark__name { font-size: 30px; letter-spacing: 6px; margin-right: -6px; }
  .card--front .wordmark__tag { font-size: 11.5px; letter-spacing: 5px; margin-right: -5px; margin-top: 10px; }
  .card--back .wordmark { left: 0; right: 0; top: 122px; text-align: center; }
  .card--back .wordmark__name { font-size: 44px; letter-spacing: 9px; margin-right: -9px; }
  .card--back .wordmark__tag { font-size: 16px; letter-spacing: 8px; margin-right: -8px; margin-top: 14px; }

  .person { position: absolute; left: 38px; top: 152px; }
  .person__name { font-size: 20px; font-weight: 700; letter-spacing: 0.2px; }
  .person__role { font-size: 14px; margin-top: 4px; }

  .divider { position: absolute; left: 38px; right: 38px; top: 208px; border-top: 1px solid var(--rule); }

  .contact { position: absolute; left: 38px; top: 228px; list-style: none; font-size: 14px; line-height: 17.5px; }
  .contact li { display: flex; align-items: center; gap: 7px; }
  .contact svg { width: 12px; height: 12px; flex: none; }

  .address { position: absolute; right: 38px; top: 228px; font-size: 14px; line-height: 17.5px; text-align: right; font-style: normal; }
</style>
</head>
<body>
  <section class="card card--front">
    <div class="wordmark">
      <div class="wordmark__name">NORTHGATE</div>
      <div class="wordmark__tag">INJURY COUNSEL</div>
    </div>
    <div class="person">
      <div class="person__name">DANA WHITFIELD</div>
      <div class="person__role">Attorney</div>
    </div>
    <div class="divider"></div>
    <ul class="contact">
      <li>
        <svg viewBox="0 0 12 12" aria-hidden="true"><path d="M2.4 1h2l.9 2.4-1.2.9a6.5 6.5 0 0 0 3.6 3.6l.9-1.2 2.4.9v2c0 .6-.5 1.1-1.1 1.1A9.4 9.4 0 0 1 1.3 2.1C1.3 1.5 1.8 1 2.4 1z" fill="var(--ink)"/></svg>
        312-555-0147
      </li>
      <li>
        <svg viewBox="0 0 12 12" aria-hidden="true"><rect x="0.5" y="2.5" width="11" height="7.5" fill="var(--ink)"/><path d="M0.8 2.8 6 6.8l5.2-4" stroke="var(--card)" stroke-width="1" fill="none"/></svg>
        info@northgatecounsel.com
      </li>
      <li>
        <svg viewBox="0 0 12 12" aria-hidden="true" fill="none" stroke="var(--ink)" stroke-width="0.9"><circle cx="6" cy="6" r="5.2"/><ellipse cx="6" cy="6" rx="2.3" ry="5.2"/><path d="M0.8 6h10.4M1.6 3.4h8.8M1.6 8.6h8.8"/></svg>
        www.northgatecounsel.com
      </li>
    </ul>
    <address class="address">
      240 West Lakeview Avenue<br>
      Suite 1800<br>
      Chicago, IL 60601
    </address>
  </section>

  <section class="card card--back">
    <div class="wordmark">
      <div class="wordmark__name">NORTHGATE</div>
      <div class="wordmark__tag">INJURY COUNSEL</div>
    </div>
  </section>
</body>
</html>
```